BRIMWELL TAVERN FRIDAY MAY 3

Flyer design for bar/nightclub event. Trying to keep a general theme with their flyers (see below) but would like to add some neon or some pop to it.

TEXT:

Brimwell Bar & Lounge Presents

MOONTIDE FRIDAYS
GRAND OPENING EVENT

PURE HOUSE MUSIC W/

VERNOX
TOMAS VEREK
BENTLER & MAJOR DRIFT

21+
9PM-130AM
418 K STREET DAVIS CA

Target Market(s)

House/dance music crowd.

Industry/Entity Type

Night Club

Font styles to use
Sans Serif

Colors
9bcb3c
fbee3d
ffffff

Requirements
Must have
• Large DJ names
Nice to have
• General theme of the attached flyers. Neon colors that stick with the theme. Anything else that looks cool will be considered

```html
<!DOCTYPE html>
<html lang="en">
<head>
<meta charset="utf-8">
<title>Moontide Fridays – Brimwell Bar &amp; Lounge</title>
<link rel="stylesheet" href="https://fonts.googleapis.com/css2?family=Montserrat:wght@400;600;700;800;900&display=swap">
<style>
  :root {
    --bg: #e9e9e9;
    --flyer-black: #050505;
    --white: #ffffff;
    --neon-green: #9bcb3c;
    --neon-yellow: #fbee3d;
    --ink: #111111;
    --photo-dark: #0b0e06;
    --photo-mid: #1c2a10;
  }
  * { box-sizing: border-box; margin: 0; padding: 0; }
  html, body { width: 1200px; height: 800px; overflow: hidden; }
  body {
    background: var(--bg);
    font-family: "Montserrat", sans-serif;
    position: relative;
  }
  .flyer {
    position: absolute;
    left: 340px; top: 30px;
    width: 520px; height: 740px;
    background: var(--flyer-black);
    overflow: hidden;
    box-shadow: 0 6px 18px rgba(0,0,0,.18);
  }
  .venue-mark {
    position: absolute;
    left: 50%; top: 30px;
    transform: translateX(-50%);
    display: flex; align-items: center; gap: 10px;
    border: 2px solid var(--neon-green);
    padding: 7px 14px 7px 7px;
  }
  .venue-mark__square {
    width: 30px; height: 30px;
    background: var(--neon-green);
  }
  .venue-mark__name {
    color: var(--white);
    font-weight: 700;
    font-size: 14px;
    letter-spacing: .5px;
    white-space: nowrap;
  }
  .event-title {
    position: absolute;
    left: 0; right: 0; top: 104px;
    text-align: center;
    color: var(--neon-green);
    font-weight: 900;
    font-size: 74px;
    line-height: 78px;
    letter-spacing: 1px;
    text-shadow: 0 0 8px rgba(155,203,60,.7), 0 0 22px rgba(155,203,60,.45);
  }
  .event-title__line { display: block; }
  .event-title__line--second { color: var(--white); text-shadow: 0 0 10px rgba(255,255,255,.45); }
  .event-subtitle {
    position: absolute;
    left: 0; right: 0; top: 278px;
    text-align: center;
    color: var(--neon-yellow);
    font-size: 15px;
    font-weight: 600;
    letter-spacing: 3px;
  }
  .time-badge {
    position: absolute;
    right: 28px; top: 318px;
    width: 96px; height: 96px;
    border-radius: 50%;
    background: var(--neon-yellow);
    border: 3px solid var(--flyer-black);
    box-shadow: 0 0 0 2px var(--neon-yellow), 0 0 18px rgba(251,238,61,.55);
    display: flex; flex-direction: column;
    align-items: center; justify-content: center;
    color: var(--ink);
    font-weight: 800;
    font-size: 16px;
    line-height: 1.1;
    text-align: center;
  }
  .time-badge__to { font-size: 11px; font-weight: 700; }
  .crowd-photo {
    position: absolute;
    left: 0; top: 330px;
    width: 520px; height: 330px;
    background: linear-gradient(180deg, var(--photo-dark) 0%, var(--photo-mid) 55%, var(--photo-dark) 100%);
  }
  .lineup {
    position: absolute;
    left: 34px; top: 432px;
    padding-left: 14px;
    border-left: 2px solid var(--neon-green);
  }
  .lineup__intro {
    color: var(--neon-yellow);
    font-size: 15px;
    font-weight: 600;
    letter-spacing: 1px;
    padding-bottom: 8px;
    margin-bottom: 8px;
    border-bottom: 1px solid var(--white);
    width: 220px;
  }
  .lineup__dj {
    color: var(--white);
    font-size: 27px;
    font-weight: 800;
    line-height: 1.25;
    white-space: nowrap;
  }
  .lineup__dj--accent { color: var(--neon-green); }
  .age-limit {
    position: absolute;
    right: 26px; top: 600px;
    color: var(--neon-yellow);
    font-size: 16px;
    font-weight: 800;
  }
  .footer-band {
    position: absolute;
    left: 0; bottom: 0;
    width: 520px; height: 110px;
  }
  .address {
    position: absolute;
    left: 0; right: 0; bottom: 36px;
    text-align: center;
    color: var(--ink);
    font-size: 14px;
    font-weight: 600;
    letter-spacing: 1px;
  }
</style>
</head>
<body>
  <main class="flyer">
    <div class="crowd-photo" role="img" aria-label="Photograph of a dark night-time scene behind the lineup"></div>

    <div class="venue-mark">
      <span class="venue-mark__square"></span>
      <span class="venue-mark__name">BRIMWELL BAR &amp; LOUNGE</span>
    </div>

    <h1 class="event-title">
      <span class="event-title__line">MOONTIDE</span>
      <span class="event-title__line event-title__line--second">FRIDAYS</span>
    </h1>

    <p class="event-subtitle">GRAND OPENING EVENT</p>

    <div class="time-badge">
      <span>9PM</span>
      <span class="time-badge__to">to</span>
      <span>1:30AM</span>
    </div>

    <div class="lineup">
      <p class="lineup__intro">PURE HOUSE MUSIC W/</p>
      <p class="lineup__dj">DJ VERNOX</p>
      <p class="lineup__dj lineup__dj--accent">DJ TOMAS VEREK</p>
      <p class="lineup__dj">DJ BENTLER &amp; MAJOR DRIFT</p>
    </div>

    <p class="age-limit">Age 21+</p>

    <svg class="footer-band" viewBox="0 0 520 110" preserveAspectRatio="none" aria-hidden="true">
      <path fill="#ffffff" d="M0 22 L30 18 L55 24 L90 15 L120 21 L160 14 L200 20 L240 12 L280 19 L320 13 L360 20 L400 12 L440 18 L480 10 L520 16 L520 110 L0 110 Z"/>
    </svg>
    <p class="address">418 K STREET DAVIS CA</p>
  </main>
</body>
</html>
```